Bluewater Motor Finance Home Page

We need a desktop version mock up (we will base our mobile version off of this) of a website homepage for our auto loan business, Bluewater Motor Finance. This does not need to be a functioning site, just a home page mock up. We are based in the metro St. Louis, MO area. We offer "guaranteed" auto loans for all credit types. We specialize in financing for bad/no credit customers. We are able to help rebuild these type of customers' credit, all while putting them in a great late model vehicle they'll love. Our online credit app takes less than 60 seconds, doesn't require a SS# and gives a free credit score if they fill it out within 3 minutes. We are looking for an outside perspective to help us in this design process. We are not completely sure what we want, but we do want it to be professional and secure looking, all while being unique and aesthetically pleasing. We want the customer to be able to put in their zip code to be directed to the right location that can get them pre approved. I attached a wireframe with some stuff we'd like to include, but in no way does it have to be in the same layout or the same ideas. We want everyone to "go crazy" with their creative side on this. Our current site is awful, here is a link to get a better idea: www.bluewatermotorfinance-example.com. Attached is our logo too, base colors off of it. Watch our video that is also attached for a better idea.

Target Market(s)

Residents of the St. Louis Missouri Metro Area that need an auto loan. 24-55 Male and Female - Lots of "urban market" customers.

Industry/Entity Type

Loan

Number of Pages Required

1 page

Colors
9bcb3b

Requirements
Must have
• An area where the customer can enter their zip code - Be creative!
Nice to have
• See wireframe attachment for ideas - Be creative!

```html
<!DOCTYPE html>
<html lang="en">
<head>
<meta charset="utf-8">
<title>Bluewater Motor Finance — Home</title>
<link href="https://fonts.googleapis.com/css2?family=Open+Sans:wght@400;600;700&family=PT+Sans:wght@400;700&display=swap" rel="stylesheet">
<style>
:root{
  --green:#9bcb3b;
  --green-dark:#7fb02a;
  --green-deep:#6a9a1f;
  --charcoal:#2b2b2b;
  --charcoal-2:#333333;
  --ink:#333333;
  --muted:#8a8a8a;
  --light:#f1f1f1;
  --white:#ffffff;
}
*{margin:0;padding:0;box-sizing:border-box}
html,body{width:1200px;height:2628px;overflow:hidden;background:var(--white)}
body{font-family:"PT Sans",Arial,sans-serif;color:var(--ink)}
.page{position:relative;width:1200px;height:2628px;overflow:hidden}
.abs{position:absolute}

/* header */
.site-header{position:absolute;left:0;top:0;width:1200px;height:110px;background:var(--charcoal);border-bottom:3px solid var(--green)}
.brand{position:absolute;left:110px;top:30px;display:flex;align-items:center;gap:12px}
.brand-mark{width:44px;height:44px;background:var(--green)}
.brand-name{font-family:"Open Sans",Arial,sans-serif;font-weight:700;font-size:19px;line-height:22px;color:var(--green);text-transform:uppercase;width:180px}
.main-nav{position:absolute;left:410px;top:47px;display:flex;align-items:center;font-family:"Open Sans",Arial,sans-serif;font-size:12.5px;font-weight:600;color:#e6e6e6;text-transform:uppercase}
.main-nav span{padding:0 14px;position:relative}
.main-nav span+span::before{content:"";position:absolute;left:-2px;top:7px;width:4px;height:4px;border-radius:50%;background:#777}
.main-nav .active{color:var(--green)}
.phone-btn{position:absolute;left:923px;top:39px;width:165px;height:38px;border:2px solid var(--green);border-radius:3px;display:flex;align-items:center;justify-content:center;gap:8px;color:var(--white);font-family:"Open Sans",Arial,sans-serif;font-size:16px;font-weight:600}

/* hero */
.hero{position:absolute;left:0;top:113px;width:1200px;height:518px}
.hero-photo{position:absolute;inset:0;background:radial-gradient(ellipse at 50% 85%,rgba(150,110,60,.45),transparent 60%),linear-gradient(180deg,#0d1216 0%,#141b20 45%,#2a2520 100%)}
.hero-title{position:absolute;left:0;top:178px;width:1200px;text-align:center;font-family:"Open Sans",Arial,sans-serif;color:var(--white);font-weight:600;font-size:39px;text-transform:uppercase;line-height:44px}
.hero-sub{position:absolute;left:0;top:225px;width:1200px;text-align:center;font-family:"Open Sans",Arial,sans-serif;color:var(--white);font-weight:600;font-size:26px;text-transform:uppercase}
.slide-arrow{position:absolute;width:22px;height:22px;border-radius:50%;background:rgba(255,255,255,.35);display:flex;align-items:center;justify-content:center}
.zip-panel{position:absolute;left:236px;top:293px;width:470px;height:116px;background:rgba(60,60,60,.75);border:1px solid rgba(255,255,255,.08)}
.zip-input{position:absolute;left:32px;top:39px;width:240px;height:42px;border:1px solid #9a9a9a;border-radius:3px;background:rgba(20,20,20,.5);color:#bdbdbd;font-size:12px;padding-left:12px;line-height:40px}
.btn-green{background:linear-gradient(180deg,#a9d64a,var(--green-dark));color:var(--white);border-radius:3px;font-family:"Open Sans",Arial,sans-serif;font-weight:600;font-size:12px;text-transform:uppercase;display:flex;align-items:center;justify-content:center;gap:6px}
.zip-btn{position:absolute;left:286px;top:39px;width:151px;height:42px}
.perks{position:absolute;left:736px;top:296px;list-style:none;color:var(--white);font-family:"Open Sans",Arial,sans-serif;font-weight:600;font-size:13.5px}
.perks li{display:flex;align-items:center;gap:7px;height:30.5px}

/* countdown band */
.apply-band{position:absolute;left:0;top:631px;width:1200px;height:126px;background:linear-gradient(180deg,#a6d245,#86b82c);display:flex;align-items:center;justify-content:center;gap:14px;color:var(--white);font-size:26px}
.timer{border:2px solid var(--white);border-radius:3px;padding:2px 14px;font-size:25px;line-height:34px}

/* testimonials */
.section-title{position:absolute;left:0;width:1200px;text-align:center;font-family:"Open Sans",Arial,sans-serif;font-weight:600;font-size:30px;color:var(--ink);text-transform:uppercase}
.avatar{position:absolute;left:116px;top:864px;width:112px;height:112px;border-radius:50%;border:4px solid #e7e7e7;background:linear-gradient(160deg,#7b8fa8,#3e4b5e)}
.quote-mark{position:absolute;left:236px;top:840px;font-family:"Open Sans",Arial,sans-serif;font-size:150px;line-height:150px;color:#eeeeee}
.testimonial-name{position:absolute;left:259px;top:870px;color:var(--green);font-size:15px}
.body-copy{font-size:11.5px;line-height:26px;color:#8a8a8a}
.testimonial-text{position:absolute;left:259px;top:898px;width:830px}
.round-arrow{position:absolute;width:20px;height:20px;border-radius:50%;background:#444;display:flex;align-items:center;justify-content:center}

/* calculator */
.calc-band{position:absolute;left:0;top:1021px;width:1200px;height:276px;background:linear-gradient(115deg,#ececec 0%,#f6f6f6 30%,#e6e6e6 55%,#f4f4f4 80%,#e9e9e9 100%)}
.calc-text{position:absolute;left:240px;top:1126px;width:720px;text-align:center}
.calc-btn{position:absolute;left:512px;top:1198px;width:178px;height:44px}

/* steps */
.step-photo{position:absolute;border:4px solid var(--white);box-shadow:0 0 0 1px #e2e2e2}
.step-title{position:absolute;font-family:"Open Sans",Arial,sans-serif;font-size:24px;color:var(--ink);text-transform:uppercase}
.step-text{position:absolute}
.divider{position:absolute;left:200px;width:800px;height:18px;background:radial-gradient(ellipse at 50% 0%,rgba(0,0,0,.08),transparent 70%)}

/* footer */
.footer-band{position:absolute;left:0;top:2211px;width:1200px;height:308px;background:linear-gradient(180deg,#9bcb3b,#74a624)}
.footer-heading{position:absolute;left:110px;top:2264px;font-family:"Open Sans",Arial,sans-serif;font-size:29px;color:var(--white);text-transform:uppercase}
.footer-text{position:absolute;left:110px;top:2318px;width:640px;color:var(--white);font-size:11.5px;line-height:24.5px;text-align:justify}
.video-label{position:absolute;left:781px;top:2246px;color:var(--white);font-family:"Open Sans",Arial,sans-serif;font-weight:600;font-size:14px;text-transform:uppercase}
.video-frame{position:absolute;left:785px;top:2278px;width:301px;height:210px;background:var(--white);padding:4px}
.video-screen{width:293px;height:175px;background:linear-gradient(160deg,#6b7387,#3a4054)}
.video-bar{height:27px;display:flex;align-items:center;gap:6px;padding:0 4px}
.video-bar i{display:block;height:10px;background:#dcdcdc;border-radius:2px}

.bottom-bar{position:absolute;left:0;top:2519px;width:1200px;height:109px;background:var(--charcoal-2)}
.bottom-links{position:absolute;left:110px;top:30px;color:#e0e0e0;font-size:11.5px;text-transform:uppercase}
.copyright{position:absolute;left:110px;top:58px;color:#bdbdbd;font-size:11.5px}
.social{position:absolute;left:968px;top:34px;display:flex;gap:9px}
.social span{width:24px;height:24px;border-radius:50%;background:#5c5c5c}
</style>
</head>
<body>
<div class="page">

  <header class="site-header">
    <div class="brand">
      <div class="brand-mark"></div>
      <div class="brand-name">Bluewater Motor Finance</div>
    </div>
    <nav class="main-nav">
      <span class="active">Home</span><span>Locations</span><span>Finance Center</span><span>About</span><span>FAQ</span><span>Contact</span>
    </nav>
    <div class="phone-btn">
      <svg width="14" height="14" viewBox="0 0 24 24"><path fill="#fff" d="M6.6 10.8a15.1 15.1 0 0 0 6.6 6.6l2.2-2.2c.3-.3.7-.4 1-.2 1.1.4 2.3.6 3.6.6.6 0 1 .4 1 1V20c0 .6-.4 1-1 1A17 17 0 0 1 3 4c0-.6.4-1 1-1h3.5c.6 0 1 .4 1 1 0 1.3.2 2.5.6 3.6.1.3 0 .7-.2 1z"/></svg>
      (800) 555-0142
    </div>
  </header>

  <section class="hero">
    <div class="hero-photo" role="img" aria-label="Night skyline of a city seen from above"></div>
    <div class="slide-arrow" style="left:14px;top:246px"><svg width="8" height="10" viewBox="0 0 8 10"><path d="M6 1 2 5l4 4" stroke="#222" stroke-width="2" fill="none"/></svg></div>
    <div class="slide-arrow" style="left:1106px;top:246px;left:1108px"><svg width="8" height="10" viewBox="0 0 8 10"><path d="M2 1l4 4-4 4" stroke="#222" stroke-width="2" fill="none"/></svg></div>
    <h1 class="hero-title">Over 30,000 Auto Loans Since 2000</h1>
    <p class="hero-sub">Pre-Approval in Under 60 Seconds!</p>
    <form class="zip-panel">
      <div class="zip-input">Enter zip code</div>
      <div class="btn-green zip-btn">
        <svg width="11" height="11" viewBox="0 0 12 12"><circle cx="6" cy="6" r="6" fill="#fff"/><path d="M5 3.5 7.5 6 5 8.5" stroke="#7fb02a" stroke-width="1.6" fill="none"/></svg>
        Get Approved
      </div>
    </form>
    <ul class="perks">
      <li><svg width="12" height="12" viewBox="0 0 12 12"><circle cx="6" cy="6" r="6" fill="#9bcb3b"/><path d="M3 6.2 5 8l4-4" stroke="#fff" stroke-width="1.6" fill="none"/></svg>No Social Security Number Required</li>
      <li><svg width="12" height="12" viewBox="0 0 12 12"><circle cx="6" cy="6" r="6" fill="#9bcb3b"/><path d="M3 6.2 5 8l4-4" stroke="#fff" stroke-width="1.6" fill="none"/></svg>Instant Approval</li>
      <li><svg width="12" height="12" viewBox="0 0 12 12"><circle cx="6" cy="6" r="6" fill="#9bcb3b"/><path d="M3 6.2 5 8l4-4" stroke="#fff" stroke-width="1.6" fill="none"/></svg>No Application Fees</li>
      <li><svg width="12" height="12" viewBox="0 0 12 12"><circle cx="6" cy="6" r="6" fill="#9bcb3b"/><path d="M3 6.2 5 8l4-4" stroke="#fff" stroke-width="1.6" fill="none"/></svg>All Credit Accepted</li>
    </ul>
  </section>

  <section class="apply-band">
    <span>Apply within</span><span class="timer">3.00</span><span>and see your credit score for free!</span>
  </section>

  <section class="testimonials">
    <h2 class="section-title" style="top:793px">Testimonials</h2>
    <div class="round-arrow" style="left:50px;top:901px"><svg width="8" height="10" viewBox="0 0 8 10"><path d="M6 1 2 5l4 4" stroke="#fff" stroke-width="2" fill="none"/></svg></div>
    <div class="round-arrow" style="left:1129px;top:901px"><svg width="8" height="10" viewBox="0 0 8 10"><path d="M2 1l4 4-4 4" stroke="#fff" stroke-width="2" fill="none"/></svg></div>
    <div class="avatar" role="img" aria-label="Portrait of a satisfied customer"></div>
    <div class="quote-mark">&ldquo;</div>
    <p class="testimonial-name">Satisfied Customer</p>
    <p class="body-copy testimonial-text">I had been turned down by three dealers before I called. The team got me approved the same afternoon, explained every term in plain language, and put me in a clean late model sedan. My payments are on time every month and my credit score has already started to climb again. I tell everyone I know about them.</p>
  </section>

  <section class="calc-band" role="img" aria-label="Soft grey faceted background"></section>
  <h2 class="section-title" style="top:1072px">Calculate Your Payment</h2>
  <p class="body-copy calc-text">Choose a vehicle price, a down payment and a loan term to see an estimated monthly payment. Numbers are estimates only and your final rate depends on approval.</p>
  <div class="btn-green calc-btn">
    <svg width="11" height="11" viewBox="0 0 12 12"><circle cx="6" cy="6" r="6" fill="#fff"/><path d="M5 3.5 7.5 6 5 8.5" stroke="#7fb02a" stroke-width="1.6" fill="none"/></svg>
    Calculate Payment
  </div>

  <section class="steps">
    <h2 class="section-title" style="top:1342px">Apply for Bad Credit Auto Loans Today</h2>

    <div class="step-photo" style="left:110px;top:1428px;width:268px;height:156px;background:linear-gradient(150deg,#c9d2dc,#2c3a4c 55%,#121a24)" role="img" aria-label="Car keys resting on a calculator"></div>
    <h3 class="step-title" style="left:403px;top:1434px">Step 1</h3>
    <p class="body-copy step-text" style="left:403px;top:1478px;width:690px">Enter your zip code and fill out our short online application. It takes less than 60 seconds and no Social Security number is needed. Finish within three minutes and we will show you your credit score for free.</p>
    <div class="divider" style="top:1629px"></div>

    <h3 class="step-title" style="left:110px;top:1693px">Step 2</h3>
    <p class="body-copy step-text" style="left:110px;top:1739px;width:680px">A finance specialist at the location nearest you reviews your application and calls you to talk through your budget, your goals and the loan options that fit. Good, bad or no credit, we work with you.</p>
    <div class="step-photo" style="left:820px;top:1691px;width:266px;height:152px;background:linear-gradient(150deg,#e9e6e2,#9a8f86 60%,#5a524c)" role="img" aria-label="Couple meeting a finance advisor at a desk"></div>
    <div class="divider" style="top:1892px"></div>

    <div class="step-photo" style="left:110px;top:1938px;width:268px;height:154px;background:linear-gradient(150deg,#a9c48a,#7d8f8a 55%,#3f4a4c)" role="img" aria-label="Hand passing car keys through a car window"></div>
    <h3 class="step-title" style="left:403px;top:1943px">Step 3</h3>
    <p class="body-copy step-text" style="left:403px;top:1990px;width:690px">Pick a great late model vehicle, sign your papers and drive home. Every on time payment is reported to help you rebuild your credit for the road ahead.</p>
    <div class="divider" style="top:2141px"></div>
  </section>

  <footer>
    <div class="footer-band"></div>
    <h2 class="footer-heading">Bluewater Motor Finance</h2>
    <p class="footer-text">Bluewater Motor Finance has helped drivers across the St. Louis metro area get behind the wheel since 2000. We specialize in auto loans for customers with bad credit, no credit or past bankruptcies, and we offer guaranteed financing for every credit type. Our goal is simple: put you in a reliable late model vehicle you will love while helping you rebuild your credit one payment at a time. Apply online in under a minute and a local specialist will be in touch soon.</p>
    <p class="video-label">Watch Our Video</p>
    <div class="video-frame">
      <div class="video-screen" role="img" aria-label="Video still of traffic lights turning green for approval"></div>
      <div class="video-bar">
        <svg width="10" height="10" viewBox="0 0 10 10"><path d="M2 1v8l7-4z" fill="#666"/></svg>
        <i style="width:150px;background:linear-gradient(90deg,#f0a030 40%,#dcdcdc 40%)"></i>
        <i style="width:30px"></i>
        <i style="width:40px"></i>
        <i style="width:14px;background:#9bcb3b"></i>
      </div>
    </div>

    <div class="bottom-bar">
      <p class="bottom-links">Home | About | Privacy | Contact</p>
      <p class="copyright">&copy; 2016 Bluewater Motor Finance. All Rights Reserved. Created by Northgate Web Studio.</p>
      <div class="social" aria-hidden="true"><span></span><span></span><span></span><span></span></div>
    </div>
  </footer>

</div>
</body>
</html>
```